Tovel Leadership Flyer - Redesign

Tovel Consulting is looking to update and redesign our one page leave behind. This page is part of the package left with prospective clients after meetings. It explains what Tovel does. Recently, we used brush quay to create a new logo for our new business name "Tovel Leadership". We would like this new logo to replace the current "Tovel Consulting" logo. We are looking for this re-designed piece to be easy to read, clean and professional, updating the design, including the graphics and layout. We typically use shades of blue (as in the Tovel Leaderhip logo - attached).

Target Market(s)

Prospective clients

Industry/Entity Type

Management Consulting

Font styles to use
Serif
Sans Serif

Colors
3176b5
33a6d7
85cae6
0255a3
3276b5
85abd2
cfdeed
cee9f5

Requirements
Must have
• New Tovel Leadership logo in place of the Tovel Consulting logo.
• Professional design.
• Formatted so that simple copy changes can be easily made, as necessary.
Should not have
• More than one page

```html
<!DOCTYPE html>
<html lang="en">
<head>
<meta charset="utf-8">
<title>Tovel Leadership – Trifold Leave-Behind</title>
<link rel="stylesheet" href="https://fonts.googleapis.com/css2?family=Open+Sans:wght@400;600;700;800&family=Noto+Serif:ital@0;1&display=swap">
<style>
  :root {
    --navy: #0255a3;
    --blue: #3176b5;
    --sky: #33a6d7;
    --aqua: #85cae6;
    --steel: #85abd2;
    --mist: #cfdeed;
    --ice: #cee9f5;
    --white: #ffffff;
    --ink: #1d3557;
    --grey-box: #c9ccd1;
    --green: #6cb33f;
    --gold: #f3c54a;
    --page: #e8ecf0;
  }
  * { box-sizing: border-box; margin: 0; padding: 0; }
  html, body { width: 1200px; height: 768px; overflow: hidden; }
  body {
    background: var(--page);
    font-family: "Open Sans", Arial, sans-serif;
    position: relative;
  }
  .panel {
    position: absolute;
    top: 64px;
    width: 276px;
    height: 640px;
    overflow: hidden;
    box-shadow: 0 2px 10px rgba(2, 40, 80, 0.15);
  }
  .panel-bg { position: absolute; inset: 0; width: 100%; height: 100%; }
  .panel-content { position: relative; padding: 30px 24px; }

  .heading {
    font-weight: 800;
    font-size: 15px;
    letter-spacing: 0.02em;
    text-transform: uppercase;
    margin-bottom: 8px;
  }
  .body-copy { font-size: 11.5px; line-height: 1.55; margin-bottom: 12px; }
  .list { list-style: none; font-size: 11px; line-height: 1.5; margin-bottom: 16px; }
  .list li { margin-bottom: 5px; padding-left: 11px; position: relative; }
  .list li::before {
    content: ""; position: absolute; left: 0; top: 6px;
    width: 5px; height: 5px; background: currentColor; border-radius: 50%;
  }

  /* Inside left: capabilities */
  .panel--capabilities { left: 36px; color: var(--white); }
  .panel--capabilities .panel-content { padding-top: 40px; }

  /* Inside middle: products */
  .panel--products { left: 312px; color: var(--ink); }
  .panel--products .heading { color: var(--navy); }
  .panel--products .panel-content { padding-top: 44px; }

  /* Inside right: coaching & consulting */
  .panel--coaching { left: 588px; color: var(--white); }
  .panel--coaching .panel-content { padding-top: 60px; }

  /* Cover */
  .panel--cover { left: 900px; background: var(--white); }
  .brand {
    position: absolute; top: 58px; left: 0; right: 0;
    display: flex; align-items: center; justify-content: center; gap: 10px;
  }
  .brand-dot { width: 22px; height: 22px; border-radius: 50%; background: var(--navy); }
  .brand-name { font-weight: 700; font-size: 25px; color: var(--navy); }
  .company-box {
    position: absolute; top: 120px; left: 26px; right: 26px;
    height: 56px; border-radius: 6px;
    background: var(--grey-box);
    display: flex; align-items: center; justify-content: center;
    font-family: "Noto Serif", Georgia, serif;
    font-size: 16px; color: #3d4450; text-align: center;
  }
  .tagline {
    position: absolute; top: 182px; left: 26px; right: 26px;
    height: 20px; background: var(--green);
    color: var(--white); font-size: 11px; font-style: italic;
    display: flex; align-items: center; padding-left: 10px;
  }
  .cover-art {
    position: absolute; top: 226px; left: 0; right: 0; height: 300px;
    background: radial-gradient(ellipse at 50% 55%, #fff6cf 0%, var(--gold) 28%, #d98f2a 48%, var(--blue) 78%, var(--navy) 100%);
  }
  .cover-bands { position: absolute; left: 0; bottom: 0; width: 100%; height: 114px; }
</style>
</head>
<body>

  <!-- Inside left -->
  <section class="panel panel--capabilities">
    <svg class="panel-bg" viewBox="0 0 276 640" preserveAspectRatio="none" aria-hidden="true">
      <defs>
        <linearGradient id="capGrad" x1="0" y1="0" x2="0" y2="1">
          <stop offset="0" stop-color="#3176b5"/>
          <stop offset="1" stop-color="#0255a3"/>
        </linearGradient>
      </defs>
      <rect width="276" height="640" fill="url(#capGrad)"/>
      <path d="M0 560 Q140 520 276 600 L276 640 L0 640 Z" fill="#33a6d7"/>
      <path d="M0 590 Q140 560 276 625 L276 640 L0 640 Z" fill="#85cae6"/>
    </svg>
    <div class="panel-content">
      <h2 class="heading">Capabilities</h2>
      <p class="body-copy">Tovel Consulting has a broad base of leadership capability, able to apply leadership and organizational development expertise to the widest range of client requirements. In this connection, we tailor our approaches and deploy facilitators, instructors and coaches across a wide breadth of large organizations.</p>
      <p class="body-copy">We are able to deploy certified leadership coaches on a broad scale, able to meet the needs of clients simultaneously and significantly, and multiple simultaneous coaching requirements.</p>
      <p class="body-copy">In addition, we are certified to administer and interpret numerous diagnostic and development instruments including the Marlow Type Indicator, Barton ORIN-B, the Westmere Psychological Inventory (WPI), and many other vital measures for leader development.</p>
    </div>
  </section>

  <!-- Inside middle -->
  <section class="panel panel--products">
    <svg class="panel-bg" viewBox="0 0 276 640" preserveAspectRatio="none" aria-hidden="true">
      <rect width="276" height="640" fill="#ffffff"/>
      <path d="M0 0 L276 0 L276 26 Q140 10 0 30 Z" fill="#cee9f5"/>
      <path d="M0 600 Q140 570 276 590 L276 640 L0 640 Z" fill="#85cae6"/>
      <path d="M0 620 Q140 600 276 615 L276 640 L0 640 Z" fill="#0255a3"/>
    </svg>
    <div class="panel-content">
      <h2 class="heading">Our Products</h2>
      <p class="body-copy">All of our products are tailored from start to complete to fit each client's needs. We listen first, then shape our approach around what matters to our clients. With that, previous solutions have included:</p>
      <h2 class="heading">Leadership Training</h2>
      <ul class="list">
        <li>Taking Charge (new supervisor program)</li>
        <li>Leading One (leading and supporting new team members)</li>
        <li>Manager as Leader</li>
        <li>Leader Motivation (what drives us)</li>
        <li>Leading the Team (strategies, technique, and tactics for leading groups)</li>
      </ul>
      <h2 class="heading">Leadership Development</h2>
      <ul class="list">
        <li>Knowing the Leader (Oneself) testing, interpretation, analysis</li>
        <li>Individual development planning</li>
        <li>The Leading Edge Program (comprehensive, holistic approach to leader development)</li>
        <li>Listening for Leaders (the most important skill a leader can master)</li>
      </ul>
    </div>
  </section>

  <!-- Inside right -->
  <section class="panel panel--coaching">
    <svg class="panel-bg" viewBox="0 0 276 640" preserveAspectRatio="none" aria-hidden="true">
      <rect width="276" height="640" fill="#33a6d7"/>
      <path d="M0 0 L276 0 L276 20 Q140 46 0 30 Z" fill="#ffffff"/>
      <path d="M0 580 Q140 610 276 570 L276 640 L0 640 Z" fill="#3176b5"/>
    </svg>
    <div class="panel-content">
      <h2 class="heading">Executive and Leadership Coaching</h2>
      <ul class="list">
        <li>Performance coaching (focusing on current performance and results)</li>
        <li>Developmental coaching (focusing on future roles and growth)</li>
        <li>Transition coaching (for leaders moving into new roles with a goal of early success)</li>
      </ul>
      <h2 class="heading">Organizational Consulting</h2>
      <ul class="list">
        <li>Team effectiveness and alignment</li>
        <li>Organizational assessment and systems review</li>
        <li>Change management support</li>
        <li>Strategic planning and alignment</li>
      </ul>
    </div>
  </section>

  <!-- Front cover -->
  <section class="panel panel--cover">
    <svg class="panel-bg" viewBox="0 0 276 640" preserveAspectRatio="none" aria-hidden="true">
      <path d="M0 0 L276 0 L276 40 Z" fill="#0255a3"/>
      <path d="M0 0 L180 0 L0 24 Z" fill="#33a6d7"/>
    </svg>
    <div class="brand">
      <span class="brand-dot"></span>
      <span class="brand-name">Tovel Leadership</span>
    </div>
    <div class="company-box">"Managemet Consulting, LLC"</div>
    <div class="tagline">We Grow Leaders.</div>
    <div class="cover-art" role="img" aria-label="Illustration of silhouetted people joining hands in a circle atop a glowing globe"></div>
    <svg class="cover-bands" viewBox="0 0 276 114" preserveAspectRatio="none" aria-hidden="true">
      <rect width="276" height="114" fill="#0255a3"/>
      <path d="M0 0 L276 0 L276 30 Q140 50 0 22 Z" fill="#33a6d7"/>
      <path d="M0 60 Q140 44 276 70 L276 80 Q140 56 0 72 Z" fill="#85cae6"/>
    </svg>
  </section>

</body>
</html>
```